CupTradeHub

-
Below info still applicable but I wanted to highlight the point that I am looking for a design similar to the style linkloop+ with the mentioned color scheme (below). If you do that then the project is yours, I'm happy with an almost clone design. I know this is a completely different type of app but what I mean is:
- The listings to look like the linkloop+ widgets (i.e. blocks, three column, and clearly seperated)
- Adverts and listings mixed together in the results set
- Prominent listings to take up 2 or 3 of the columns instead, non prominent ones to take up 1.
- Clear spacing between the listings, as with linkloop+ widgets
- Clear seperation between menu and widgets as with linkloop+
- Search/filters and category filters on the right or left, as with linkloop+
Again, if this is not clear I want it LIKE LINKLOOP+, so far had stock template designs that weren't anything like this.
Linkloop+ is not the only site I listed for inspiration, but I think its easier at this point to just say clone the damn thing, and re purpose it for coffee. We will make additional changes at development time to make it distinct and incorporate some of the other things we were looking for.
-
Hi All,
I'm looking to get designs for a new site that allows coffee roasters, and barista equipment suppliers to sell their goods to coffee shops via an auction site. So essentially B2B bidnest targeted at the coffee market.
Pages required:
All pages:
- Logo
- Login/register links (or my account if logged in)
- links to Contact us, FAQs, Advertise with us
Homepage:
- Search bar
- List of filter categories
- Latest products section
- Advertising section
Search page:
- Listings (Image, price (buy now or current bid), postage price, no bids, time remaining to bid)
- Advertising
Listing page
- Same listing info as above but with full description, multipule images to select from, time ending and and a bid form (enter amount) or buy now button.
Login page
- Username/Password
- Alternative login via Friendora
My account:
- Link to add listings
- List of current listings
- List of current bids
- Link to purchase history
Add a listing:
- Form page to add a listing
- Requires
- Images uploads (drag to upload, as well as normal)
- Title field
- Description field
- Amount field
- Quantity field
- Postage amount field
- Category Drop down field
- End date/time picker field
That's it for functionality, with regards to design this needs to be designed in a way that is compatible with scaffoldr components (http://chirpnet.codehost.example/scaffoldr/), though scaffoldr is highly customizable so don't feel too restricted.
Styles/colours:
Site layout should be clean, and clear utilizing white space well i.e.
- http://shrt.example/qpWmT
- http://shrt.example/VbRdK
- https://circles.linkloop.example/
Also VERY much like the vantasoft "tiler" style design i.e. square boxes. If you know what I mean by this then cool, if not don't worry about it.
The logo on the other hand should have and earthy, organic feel to it.
Also, please only use fonts available from typevault fonts (http://www.typevault.example/fonts/).

```html
<!DOCTYPE html>
<html lang="en">
<head>
<meta charset="utf-8">
<title>CupTradeHub</title>
<link href="https://fonts.googleapis.com/css2?family=Rosario:wght@400;600;700&family=PT+Serif:wght@400;700&family=Noto+Sans:wght@400;600&display=swap" rel="stylesheet">
<style>
:root{
  --page:#f0f0f0;
  --white:#ffffff;
  --green:#1c6b45;
  --brown:#7a553a;
  --ink:#2b2b2b;
  --muted:#6a6a6a;
  --line:#d8d8d8;
  --band:#d5d5d5;
  --pill:#4b4b4b;
}
*{box-sizing:border-box;margin:0;padding:0}
html,body{width:1062px;height:1200px;overflow:hidden}
body{background:var(--page);font-family:"Rosario",sans-serif;color:var(--ink);position:relative}
a{color:inherit;text-decoration:none}

.site-header{position:absolute;left:0;top:0;width:1062px;height:49px;background:linear-gradient(#ffffff,#f3f3f3);box-shadow:0 1px 3px rgba(0,0,0,.18);z-index:2}
.brand{position:absolute;left:123px;top:13px;font-family:"PT Serif",serif;font-weight:700;font-size:20px;color:var(--green);letter-spacing:-.3px}
.main-nav{position:absolute;left:287px;top:14px;display:flex;font-size:12px;color:#555}
.main-nav a{padding:4px 8px;margin-right:9px;border:1px solid transparent;border-radius:3px}
.main-nav a.active{border-color:#c9c9c9;background:linear-gradient(#fff,#ececec);font-weight:700;color:var(--ink);box-shadow:0 1px 1px rgba(0,0,0,.08)}
.util-nav{position:absolute;right:123px;top:19px;font-size:10px;color:#444}
.util-nav span{margin:0 4px;color:#888}

.search-band{position:absolute;left:123px;top:49px;width:816px;height:59px;background:var(--band);border-radius:0 0 4px 4px}
.search-form{position:absolute;left:168px;top:13px;width:420px;height:35px;background:var(--green);border-radius:18px;padding:3px}
.search-form input{width:370px;height:29px;border:none;border-radius:15px;padding:0 12px;font-family:"Rosario",sans-serif;font-size:12px;color:#777;background:linear-gradient(#fff,#f4f4f4)}
.search-form svg{position:absolute;right:16px;top:9px}
.advanced-search{position:absolute;left:599px;top:22px;font-size:12px;font-weight:700;color:#333;text-decoration:underline}

.listing-tabs{position:absolute;left:123px;top:128px;width:816px;height:28px;border-bottom:1px solid var(--line);font-size:12px;display:flex;gap:23px;padding-left:2px}
.listing-tabs a.active{font-weight:700}

.product-grid{position:absolute;left:123px;top:186px;width:816px;display:grid;grid-template-columns:repeat(4,186px);column-gap:24px;row-gap:35px}
.product-card{background:var(--white);height:159px;padding:8px 9px;box-shadow:0 0 2px rgba(0,0,0,.06)}
.product-photo{width:168px;height:126px;border-radius:1px}
.photo-cup{background:linear-gradient(160deg,#e9e5df 0%,#b79a80 45%,#6e4a2e 100%)}
.photo-roaster{background:linear-gradient(180deg,#efeae0 0%,#8c8a85 55%,#3c3b39 100%)}
.photo-machine{background:linear-gradient(180deg,#f2f2ee 0%,#c9c6b3 50%,#5b5a4c 100%)}
.photo-espresso{background:linear-gradient(180deg,#f1f2f3 0%,#a9adb1 50%,#4a4c4f 100%)}
.photo-brewer{background:linear-gradient(180deg,#8d7a66 0%,#b3aea5 50%,#6a5947 100%)}
.photo-vending{background:linear-gradient(180deg,#3b3b3d 0%,#6f6f72 45%,#c4c4c4 100%)}
.card-meta{display:flex;justify-content:space-between;margin-top:7px;font-family:"Noto Sans",sans-serif;font-size:9.5px}
.card-meta .title{font-weight:600}
.card-meta .details{color:var(--muted)}

.view-more{position:absolute;left:454px;top:764px;width:153px;height:33px;border-radius:17px;background:linear-gradient(#8b6548,#6d4a31);color:#fff;font-family:"PT Serif",serif;font-size:11px;letter-spacing:.4px;display:flex;align-items:center;justify-content:center;box-shadow:0 1px 2px rgba(0,0,0,.3)}

.divider{position:absolute;left:123px;top:821px;width:816px;border-top:1px solid var(--line)}
.section-heading{font-family:"PT Serif",serif;font-weight:700;font-size:15px;color:#3a3a3a}
.tags{position:absolute;left:123px;top:838px;width:200px}
.tag-list{margin-top:14px;display:flex;flex-wrap:wrap;gap:8px 9px;width:170px}
.tag-list a{background:var(--pill);color:#fff;font-family:"PT Serif",serif;font-size:10.5px;height:25px;padding:0 11px;border-radius:13px;display:flex;align-items:center}
.tag-list a:nth-child(3){margin-left:2px}
.brands{position:absolute;left:333px;top:838px;width:200px}
.brand-list{margin-top:18px;display:grid;grid-template-columns:96px 96px;row-gap:22px}
.brand-list span{font-family:"Rosario",sans-serif;font-weight:700;font-size:14px;color:#333;display:flex;align-items:center;height:30px}
.brand-list .dot{width:10px;height:10px;border-radius:50%;background:var(--green);margin-right:5px;flex:none}
.brand-list .twoline{font-size:11px;line-height:1.1}
.advertise{position:absolute;left:545px;top:838px}
.ad-frame{position:absolute;left:-2px;top:33px;width:392px;height:107px;background:#fff;border-radius:4px;padding:5px;box-shadow:0 0 3px rgba(0,0,0,.1)}
.ad-inner{position:relative;width:100%;height:100%;background:linear-gradient(90deg,#f7f7f7,#ececec)}
.ad-copy{position:absolute;left:45px;top:26px;font-family:"Noto Sans",sans-serif}
.ad-copy strong{display:block;font-weight:400;font-size:18px;color:#555}
.ad-copy strong em{font-style:normal;color:#e07a1f}
.ad-copy small{font-size:6.5px;color:#777}
.ad-art{position:absolute;right:35px;top:4px;width:150px;height:90px;border-radius:45px 45px 45px 8px;background:linear-gradient(135deg,#f2a62b 0%,#e8622a 45%,#d6282c 100%)}

.site-footer{position:absolute;left:0;top:1000px;width:1062px;height:200px;background:#fff;border-top:1px solid #dcdcdc;font-family:"Noto Sans",sans-serif}
.footer-brand{position:absolute;left:123px;top:20px;width:185px}
.footer-brand .brand{position:static;font-size:15px}
.footer-brand p{margin-top:4px;font-size:10.5px;line-height:15px;color:#7a7a7a;letter-spacing:.2px}
.footer-col{position:absolute;top:26px;width:180px}
.footer-col h4{font-size:10.5px;font-weight:600;color:#444;letter-spacing:.4px;margin-bottom:6px}
.footer-col a{display:block;font-size:10.5px;color:#7a7a7a;line-height:20px;letter-spacing:.4px}
.footer-base{position:absolute;left:123px;top:163px;width:816px;border-top:1px solid var(--line);padding-top:12px;display:flex;justify-content:space-between;font-size:10.5px;color:#555;letter-spacing:.2px}
</style>
</head>
<body>

<header class="site-header">
  <a class="brand" href="#">CupTradeHub</a>
  <nav class="main-nav">
    <a class="active" href="#">Home</a>
    <a href="#">About</a>
    <a href="#">FAQ's</a>
    <a href="#">Signup</a>
  </nav>
  <nav class="util-nav"><a href="#">Sign in</a><span>|</span><a href="#">Advertise With Us</a><span>|</span><a href="#">Contact Us</a></nav>
</header>

<section class="search-band">
  <form class="search-form">
    <input type="text" value="Search...">
    <svg width="16" height="16" viewBox="0 0 16 16" aria-hidden="true"><circle cx="6" cy="6" r="4.5" fill="none" stroke="#fff" stroke-width="2"/><line x1="9.5" y1="9.5" x2="14.5" y2="14" stroke="#fff" stroke-width="3" stroke-linecap="round"/></svg>
  </form>
  <a class="advanced-search" href="#">Advanced Search</a>
</section>

<nav class="listing-tabs">
  <a class="active" href="#">Popular</a>
  <a href="#">Latest</a>
  <a href="#">All Products</a>
</nav>

<main class="product-grid">
  <article class="product-card"><div class="product-photo photo-cup" role="img" aria-label="Cup of black coffee on roasted beans"></div><div class="card-meta"><span class="title">Product Title</span><span class="details">Details</span></div></article>
  <article class="product-card"><div class="product-photo photo-roaster" role="img" aria-label="Countertop coffee roaster"></div><div class="card-meta"><span class="title">Product Title</span><span class="details">Details</span></div></article>
  <article class="product-card"><div class="product-photo photo-machine" role="img" aria-label="Drum coffee roasting machine"></div><div class="card-meta"><span class="title">Product Title</span><span class="details">Details</span></div></article>
  <article class="product-card"><div class="product-photo photo-machine" role="img" aria-label="Small batch roaster with hopper"></div><div class="card-meta"><span class="title">Product Title</span><span class="details">Details</span></div></article>

  <article class="product-card"><div class="product-photo photo-espresso" role="img" aria-label="Two-group espresso machine"></div><div class="card-meta"><span class="title">Product Title</span><span class="details">Details</span></div></article>
  <article class="product-card"><div class="product-photo photo-espresso" role="img" aria-label="Espresso machine with grinder"></div><div class="card-meta"><span class="title">Product Title</span><span class="details">Details</span></div></article>
  <article class="product-card"><div class="product-photo photo-brewer" role="img" aria-label="Twin commercial coffee brewers"></div><div class="card-meta"><span class="title">Product Title</span><span class="details">Details</span></div></article>
  <article class="product-card"><div class="product-photo photo-vending" role="img" aria-label="Automatic coffee vending machine"></div><div class="card-meta"><span class="title">Product Title</span><span class="details">Details</span></div></article>

  <article class="product-card"><div class="product-photo photo-cup" role="img" aria-label="Cup of black coffee on roasted beans"></div><div class="card-meta"><span class="title">Product Title</span><span class="details">Details</span></div></article>
  <article class="product-card"><div class="product-photo photo-roaster" role="img" aria-label="Countertop coffee roaster"></div><div class="card-meta"><span class="title">Product Title</span><span class="details">Details</span></div></article>
  <article class="product-card"><div class="product-photo photo-machine" role="img" aria-label="Drum coffee roasting machine"></div><div class="card-meta"><span class="title">Product Title</span><span class="details">Details</span></div></article>
  <article class="product-card"><div class="product-photo photo-machine" role="img" aria-label="Small batch roaster with hopper"></div><div class="card-meta"><span class="title">Product Title</span><span class="details">Details</span></div></article>
</main>

<a class="view-more" href="#">VIEW MORE ENTRIES</a>

<div class="divider"></div>

<section class="tags">
  <h3 class="section-heading">Tags:</h3>
  <div class="tag-list">
    <a href="#">Coffee Roster</a><a href="#">Barista</a>
    <a href="#">Coffee</a><a href="#">Equipments</a>
    <a href="#">Barista</a><a href="#">Coffee</a>
  </div>
</section>

<section class="brands">
  <h3 class="section-heading">Popular Brands:</h3>
  <div class="brand-list">
    <span>tablora</span>
    <span><i class="dot"></i>huddlr</span>
    <span class="twoline">Twin Sprout<br>Tech</span>
    <span>hearthly</span>
  </div>
</section>

<section class="advertise">
  <h3 class="section-heading">Advertise:</h3>
  <div class="ad-frame">
    <div class="ad-inner">
      <div class="ad-copy"><strong>sample<em>text</em></strong><small>Suspendisse euismod venenatis.</small></div>
      <div class="ad-art" role="img" aria-label="Abstract splash of red and orange petals"></div>
    </div>
  </div>
</section>

<footer class="site-footer">
  <div class="footer-brand">
    <a class="brand" href="#">CupTradeHub</a>
    <p>Lorem Ipsum is simply dummy text of the printing and typesetting industry. Lorem Ipsum has been the industry's standard dummy text ever since the 1500s.</p>
  </div>
  <div class="footer-col" style="left:333px">
    <h4>Link Heading 1:</h4>
    <a href="#">Navigation Link 1</a><a href="#">Navigation Link 2</a><a href="#">Navigation Link 3</a><a href="#">Navigation Link 4</a><a href="#">Navigation Link 5</a>
  </div>
  <div class="footer-col" style="left:543px">
    <h4>Link Heading 2:</h4>
    <a href="#">Navigation Link 1</a><a href="#">Navigation Link 2</a><a href="#">Navigation Link 3</a><a href="#">Navigation Link 4</a><a href="#">Navigation Link 5</a>
  </div>
  <div class="footer-col" style="left:753px">
    <h4>Link Heading 3:</h4>
    <a href="#">Navigation Link 1</a><a href="#">Navigation Link 2</a><a href="#">Navigation Link 3</a><a href="#">Navigation Link 4</a><a href="#">Navigation Link 5</a>
  </div>
  <div class="footer-base">
    <span>Copyright © 2013 Cup Trade Hub | All Rights Reserved</span>
    <span>Privacy Policy | Legal | Contact Us</span>
  </div>
</footer>

</body>
</html>
```